Redesign of Website

We need an overhaul of our website. I've attached our current logo files. Please visit www.pelvorix.com for our current website for information about our company. We are looking for the same type of website (information-based only) so no need for any online store, payments, interactive stuff or anything like that...basically looking for a fresh new look! Also please make sure this design will be mobile-friendly. Thanks!

```html
<!DOCTYPE html>
<html lang="en">
<head>
<meta charset="utf-8">
<title>Pelvorix Consultants</title>
<link href="https://fonts.googleapis.com/css2?family=Roboto:wght@400;500;700&display=swap" rel="stylesheet">
<style>
:root{
  --navy:#0b2a68;
  --royal:#0a3a8a;
  --footer:#0c2763;
  --footer-deep:#0a2259;
  --text:#555a60;
  --white:#ffffff;
  --rule:#3e5894;
}
*{margin:0;padding:0;box-sizing:border-box}
html,body{width:991px;height:1200px;overflow:hidden;background:var(--white);font-family:"Roboto",Arial,sans-serif}
.page{position:relative;width:991px;height:1200px}
.topbar{height:29px;background:var(--royal);color:var(--white);font-size:13px;display:flex;justify-content:flex-end;align-items:center;gap:49px;padding-right:35px}
.header{height:90px;position:relative}
.brand{position:absolute;left:100px;top:24px;font-size:26px;font-weight:700;color:var(--navy);display:flex;align-items:center;gap:8px}
.brand-square{width:14px;height:14px;background:var(--navy)}
.nav{position:absolute;left:288px;top:41px;display:flex;gap:9px;font-size:16px;font-weight:700;color:var(--royal)}
.hero{position:absolute;top:119px;left:0;width:991px;height:336px;background:linear-gradient(100deg,#6e7e8e 0%,#8b6f5c 40%,#4b5f86 70%,#1d4a9c 100%)}
.hero-panel{position:absolute;left:0;top:72px;width:813px;height:184px;background:rgba(20,28,45,.72)}
.hero-title{position:absolute;left:133px;top:105px;font-size:23px;font-weight:700;color:var(--white)}
.hero-text{position:absolute;left:131px;top:143px;width:670px;font-size:20px;line-height:22.5px;color:var(--white)}
.arrow{position:absolute;top:148px}
.arrow-left{left:18px}.arrow-right{right:18px}
.intro{position:absolute;left:113px;top:486px;width:780px}
.intro-title{font-size:21px;font-weight:700;color:var(--navy);display:flex;align-items:center;gap:6px;margin-bottom:20px}
.intro-title .divider{width:1px;height:22px;background:#999;margin:0 2px}
.intro-title .name{font-weight:500;letter-spacing:1.5px;color:#4a4f55}
.intro p{font-size:15.5px;line-height:18.6px;color:var(--text);margin-bottom:18px}
.band{position:absolute;left:0;top:919px;width:991px;height:17px;background:var(--footer)}
.footer{position:absolute;left:0;top:952px;width:991px;height:248px;background:var(--footer)}
.footer-brand{position:absolute;left:64px;top:60px;font-size:24px;font-weight:700;color:#6f86b8;display:flex;align-items:center;gap:7px}
.footer-brand .brand-square{background:#6f86b8}
.col-rule{position:absolute;top:34px;width:1px;height:133px;background:var(--rule)}
.footer-list{position:absolute;list-style:none;color:#c9d3e8;font-size:14px;line-height:20px}
.socials{position:absolute;left:745px;top:78px;display:flex;gap:2px}
.socials span{width:16px;height:16px;border-radius:3px;background:#c9d3e8}
.legal{position:absolute;left:0;bottom:0;width:991px;height:44px;border-top:1px solid #1c3a7a;background:var(--footer-deep);color:#c9d3e8;font-size:11px;display:flex;align-items:center;justify-content:center}
</style>
</head>
<body>
<div class="page">
  <div class="topbar"><span>Call us now! 700 5120 418</span><span>Find our Location</span></div>
  <header class="header">
    <div class="brand"><span class="brand-square"></span>Pelvorix</div>
    <nav class="nav"><span>HOME</span><span>ABOUT</span><span>CONTACT</span><span>SERVICE</span></nav>
  </header>
  <section class="hero" role="img" aria-label="Photo of a brick building under construction with scaffolding and a worker">
    <div class="hero-panel"></div>
    <h1 class="hero-title">Property Condition Reports</h1>
    <p class="hero-text">Before moving ahead on any loan approval, financial institutions need to know the condition of existing structures. Our professional staff will give you the details you need to make sound business decisions</p>
    <svg class="arrow arrow-left" width="22" height="30" viewBox="0 0 22 30"><path d="M18 3 6 15l12 12" fill="none" stroke="#fff" stroke-width="3"/></svg>
    <svg class="arrow arrow-right" width="22" height="30" viewBox="0 0 22 30"><path d="M4 3l12 12L4 27" fill="none" stroke="#fff" stroke-width="3"/></svg>
  </section>
  <main class="intro">
    <h2 class="intro-title">Pelvorix.com – <span class="divider"></span><span class="name">PELVORIX CONSULTANTS</span></h2>
    <p>With over 25 years experience we provide customized and comprehensive inspection services to financial institution involved in construction and loan management in New York, New Jersey, Pennsylvania and surrounding areas.</p>
    <p>The firm’s professional staff bring years of engineering, environmental, building, and real estate experience to work for our clients.</p>
    <p>Pelvorix provides our clients with in-depth plan &amp; cost, construction funding, environmental and property condition reports.</p>
    <p>Pelvorix will give you the essential facts that are critical for solid business decision making and ongoing loan management.</p>
    <p>Pelvorix Consultants’ projects range from single family homes to $30,000,000 mid-rise buildings to $60,000,000 casino renovation projects. Our clients have come to think of us as part of their trusted teamThey turn to us to evaluate plans, costs and approvals before they commit to a construction loan; and enlistour services throughout the construction process to ensure that all phases of the project are funded properlyand documented accordingly. Pelvorix understands the delicate balance required in order to protect the client’s position and simultaneously keep their costumers satisfied.</p>
  </main>
  <div class="band"></div>
  <footer class="footer">
    <div class="footer-brand"><span class="brand-square"></span>Pelvorix</div>
    <span class="col-rule" style="left:287px"></span>
    <span class="col-rule" style="left:507px"></span>
    <span class="col-rule" style="left:714px"></span>
    <ul class="footer-list" style="left:309px;top:54px"><li>Home</li><li>About</li><li>Contact</li><li>Services</li></ul>
    <ul class="footer-list" style="left:544px;top:52px"><li>Map</li><li>Address</li></ul>
    <ul class="footer-list" style="left:746px;top:52px"><li>Follow Us</li></ul>
    <div class="socials"><span></span><span></span><span></span><span></span></div>
    <div class="legal">Copyright © 2019 | Pelvorix.com | 418 N Ridgeline Ave #112 Ridgeline Township, NJ 07990 | 973-555-0142</div>
  </footer>
</div>
</body>
</html>
```